Pelvar Modellwerk.Brenn GmbH needed a letterhead template

For English scroll down. We need a letterhead template and since we already have our logo design successfully with you, we now want to also design the letterhead with you. Down in the uploaded file you see what is important and what should definitely be seen on our template. The template should be like the homepage (www.modellwerk.brenn) held in red, blue and white. We need a letter-head submission. In the bottom in the chapter "databases uploading" you can find the most important things, did must be on the submission. The submission shoulderstand be in the colors blue, red and white like our homepage (www.modellwerk.brenn).

```html
<!DOCTYPE html>
<html lang="de">
<head>
<meta charset="utf-8">
<title>Pelvar Modellwerk.Brenn GmbH – Briefpapier</title>
<link rel="stylesheet" href="https://fonts.googleapis.com/css2?family=Open+Sans:wght@400;600;700&display=swap">
<style>
  :root {
    --brand-blue: #2f6db5;
    --brand-blue-soft: #3a73ae;
    --brand-red: #c21f26;
    --paper: #ffffff;
    --ink: #1a1a1a;
    --backdrop: #d4d4d4;
  }
  * { margin: 0; padding: 0; box-sizing: border-box; }
  html, body {
    width: 1200px; height: 790px; overflow: hidden;
    background: var(--backdrop);
    font-family: "Open Sans", Arial, sans-serif;
    color: var(--ink);
  }
  .letterhead {
    position: absolute; left: 335px; top: 20px;
    width: 530px; height: 750px;
    background: var(--paper);
    box-shadow: 0 2px 10px rgba(0,0,0,.18);
    overflow: hidden;
  }
  .header-accent {
    position: absolute; top: 22px; right: 0;
    width: 290px; height: 80px;
    background: linear-gradient(100deg, rgba(58,115,174,0) 0%, rgba(58,115,174,.55) 45%, rgba(194,31,38,.6) 100%);
  }
  .brand { position: absolute; left: 28px; top: 26px; display: flex; align-items: center; gap: 7px; }
  .brand-dot { width: 16px; height: 16px; border-radius: 50%; background: var(--brand-red); }
  .brand-name { font-size: 19px; font-weight: 700; color: var(--brand-blue); letter-spacing: .2px; }
  .sender { position: absolute; left: 34px; top: 54px; font-size: 7.5px; line-height: 1.3; font-style: normal; }
  .footer {
    position: absolute; left: 30px; right: 30px; bottom: 22px;
    display: flex; justify-content: space-between; align-items: flex-start;
    font-size: 9.5px; line-height: 1.35;
  }
  .footer-contact { margin-top: 26px; }
  .footer-bank { margin-top: 40px; }
  .footer-band { position: absolute; left: 0; right: 0; bottom: 0; height: 7px; display: flex; }
  .footer-band span { flex: 1; }
  .band-blue { background: var(--brand-blue); }
  .band-red { background: var(--brand-red); }
</style>
</head>
<body>
  <main class="letterhead">
    <div class="header-accent" role="img" aria-label="Dekorative Wellenbänder in Blau und Rot"></div>

    <div class="brand">
      <span class="brand-dot"></span>
      <span class="brand-name">Modellwerk.Brenn</span>
    </div>

    <address class="sender">
      Pelvar Modellwerk.Brenn GmbH<br>
      Lindenweg 12<br>
      6020 Brennau, Tirol<br>
      Österreich
    </address>

    <footer class="footer">
      <div class="footer-company">
        Geschäftsführer Dr. Amsel Lukas<br>
        Lindenweg 12<br>
        6020 Brennau, Tirol<br>
        Österreich
      </div>
      <div class="footer-contact">
        Telefon: 0800 XX XX XX<br>
        Mail: contact@modellwerk.brenn<br>
        Web: www.modellwerk.brenn
      </div>
      <div class="footer-bank">
        Talbank XXXX<br>
        IBAN: ATXX XXXX XXXX XXXX<br>
        BIC: XXXX<br>
        UID-Nr.: ATUXXXXX
      </div>
    </footer>

    <div class="footer-band">
      <span class="band-blue"></span>
      <span class="band-red"></span>
      <span class="band-blue"></span>
    </div>
  </main>
</body>
</html>
```